Pastry Trade Institute Website Homepage Revision

I need the "homepage" to the new Northfield Pastry Trade Institute to reworked. The current homepage is dull. It needs the attention of a professional graphic artist so it delivers a professionally finished feel and look. I have included the current URL for your viewing (builds.vorlimo.com/bridal-torte/cms/ ) to see where we are in the development phase. The elements on the homepage are all necessary and the colors are correct. I have also included the original Word document for the page (you can extract the RGB values and images from the doc). To be clear, I am not looking to recreate all the web pages, just the homepage. It needs to be responsive and stretched.

Target Market(s)

All bakers who sell wedding cakes in the United States

Number of Pages Required

1 page

Font styles to use
Other font styles liked:
• see the Word Document

Requirements
Must have
• It must have the elements already in the original mock up. That includes the colors and fonts.

```html
<!DOCTYPE html>
<html lang="en">
<head>
<meta charset="utf-8">
<title>Northfield Pastry Trade Institute</title>
<link href="https://fonts.googleapis.com/css2?family=Roboto:wght@300;400;500;700&family=Kalam:wght@400&display=swap" rel="stylesheet">
<style>
:root{
  --plum:#9a1a73;
  --teal:#2cbfbd;
  --orange:#f6a11a;
  --page:#f1f1f1;
  --ink:#444;
  --muted:#777;
  --wood:#6e4a38;
  --wood-dark:#3f2a20;
  --white:#fff;
}
*{box-sizing:border-box;margin:0;padding:0}
html,body{width:1200px;height:3879px;overflow:hidden}
body{font-family:'Roboto',Arial,sans-serif;background:var(--page);color:var(--ink);position:relative}
.abs{position:absolute}
.site-nav{left:0;top:0;width:1200px;height:78px;background:var(--white);display:flex;align-items:center;padding:0 72px;z-index:3}
.site-nav ul{display:flex;list-style:none;gap:22px;font-size:12.5px;font-weight:500;color:#333;text-transform:uppercase;white-space:nowrap}
.site-nav li.active{color:var(--plum);border-bottom:2px solid var(--plum);padding-bottom:3px}
.member-login{margin-left:auto;border:1.5px solid var(--plum);color:var(--plum);font-size:12.5px;font-weight:500;padding:10px 18px;border-radius:4px;text-transform:uppercase;white-space:nowrap}
.hero{left:0;top:78px;width:1200px;height:560px;background:linear-gradient(160deg,#7a5240 0%,var(--wood) 40%,var(--wood-dark) 100%)}
.hero-name{left:0;top:250px;width:1200px;text-align:center;font-size:58px;font-weight:700;color:#e8c39c;letter-spacing:1px}
.hero-wave{left:0;top:490px}
.intro{left:0;top:690px;width:1200px;text-align:center;font-size:31px;line-height:54px;color:#555;font-weight:500}
.squiggle{left:480px;top:795px}
.press-row{left:72px;top:822px;width:1056px;display:flex;justify-content:space-between;align-items:center}
.press-badge{width:74px;height:38px;background:#c9c9c9;border-radius:4px}
.press-badge.round{width:44px;height:44px;border-radius:50%}
.video{left:72px;top:910px;width:606px;height:326px;background:linear-gradient(90deg,#c9d3da 0%,#dfe4e7 45%,#eef0f1 100%);box-shadow:0 3px 8px rgba(0,0,0,.35);border:3px solid #fff}
.video-quote{left:360px;top:70px;width:220px;color:#222;font-size:21px;font-weight:700;line-height:1.3}
.video-quote .q{color:#8b1e2a;font-size:23px;margin-bottom:18px;display:block}
.optin{left:703px;top:910px;width:422px;height:326px;background:var(--teal);padding:22px 38px}
.optin h2{color:#fff;font-size:25px;font-weight:500;line-height:1.25;margin-bottom:24px}
.field{background:#fff;height:38px;border-radius:3px;font-size:14px;color:#999;padding:11px 14px;margin-bottom:18px}
.btn{background:var(--orange);color:#fff;font-weight:700;font-size:17px;text-transform:uppercase;text-align:center}
.optin .btn{width:184px;height:48px;line-height:48px;margin:0 auto}
.teal-band{left:0;top:1260px}
.swoosh{left:515px;top:1366px}
.path-card{top:1417px;width:244px;height:207px;background:#fff;box-shadow:0 2px 6px rgba(0,0,0,.25);text-align:center;padding-top:18px}
.path-card .mark{display:block;margin:0 auto 8px}
.path-card h3{font-family:'Kalam',cursive;font-weight:400;color:var(--plum);font-size:27px;line-height:37px;padding:0 16px}
.path-card .more{color:var(--orange);font-size:13px;margin-top:10px}
.feature{top:1766px;width:336px;height:324px;background:#fff;box-shadow:0 2px 6px rgba(0,0,0,.22)}
.feature-img{left:0;top:0;width:336px;height:208px}
.feature-wave{left:0;top:160px}
.feature p{position:absolute;left:20px;top:218px;width:296px;font-size:13.5px;line-height:1.55;color:var(--muted)}
.method-head{left:0;top:2262px;width:1200px;text-align:center;color:var(--plum);font-size:30.5px;font-weight:500;line-height:46px}
.founder{left:72px;top:2475px;width:249px;height:354px}
.founder-photo{width:249px;height:318px;background:linear-gradient(180deg,#ececec 0%,#dcd6d0 50%,#d2d2d2 100%)}
.founder-name{width:249px;height:36px;background:var(--plum);color:#fff;text-align:center;font-weight:700;font-size:17px;line-height:36px}
.method-copy{left:434px;top:2470px;width:691px;font-size:14.5px;line-height:1.6;color:#555}
.method-copy p{margin-bottom:20px}
.advisory{left:434px;top:2741px;width:691px;height:220px;background:#d3e0e0;padding:20px 22px}
.advisory h3{color:var(--plum);font-size:30px;font-weight:500;margin-bottom:22px}
.advisory p{color:var(--plum);font-size:17px;line-height:1.45}
.advisory strong{display:block;margin-top:24px;font-size:21px}
.insider-band{left:0;top:3030px}
.insider{left:0;top:3125px;width:1200px;text-align:center;color:#fff}
.insider h2{font-size:32px;font-weight:500;margin-bottom:26px}
.insider p{font-size:16px;line-height:1.8;width:820px;margin:0 auto}
.insider-form{left:164px;top:3301px;display:flex;gap:28px}
.insider-form .field{width:332px;height:38px;margin:0}
.insider-form .btn{width:150px;height:38px;line-height:38px;font-size:15px}
.social{left:0;top:3498px;width:1200px;display:flex;justify-content:center;gap:24px}
.social span{width:38px;height:38px;border:2px solid var(--plum);border-radius:50%}
.rule{left:0;top:3566px;width:1200px;height:1px;background:#ddd}
.footer-cols{left:75px;top:3596px;width:1076px;display:grid;grid-template-columns:repeat(4,269px)}
.footer-col h4{color:var(--plum);font-size:17px;font-weight:700;margin-bottom:10px}
.footer-col li{list-style:none;font-size:14px;color:#555;line-height:34px;white-space:nowrap}
</style>
</head>
<body>

<nav class="site-nav abs">
  <ul>
    <li class="active">Home</li><li>Cal's Story</li><li>Marketing Solutions</li><li>Sales Solutions</li><li>Hire Us</li><li>Contact</li><li>Partner With Us</li><li>Blog</li><li>My Courses</li>
  </ul>
  <div class="member-login">Member Login</div>
</nav>

<header class="hero abs" role="img" aria-label="Wood panel wall backdrop behind the institute name"></header>
<div class="hero-name abs">Northfield Pastry Trade Institute</div>
<svg class="hero-wave abs" width="1200" height="150" viewBox="0 0 1200 150">
  <path d="M0 20 C300 130 700 40 1200 0 L1200 150 L0 150Z" fill="var(--page)"/>
  <path d="M0 20 C300 130 700 40 1200 0 L1200 40 C800 70 380 150 0 120Z" fill="var(--plum)"/>
  <path d="M0 120 C380 150 800 70 1200 40 L1200 60 C800 90 400 160 0 150Z" fill="#fff"/>
</svg>

<div class="intro abs">Our research is not just a game changer. It is the game changer.<br>We're rewriting the book for selling wedding cakes!</div>
<svg class="squiggle abs" width="240" height="20"><path d="M4 14 C70 2 160 2 236 8" stroke="var(--plum)" stroke-width="3" fill="none"/></svg>

<div class="press-row abs">
  <span class="press-badge"></span><span class="press-badge"></span><span class="press-badge"></span><span class="press-badge round"></span><span class="press-badge"></span><span class="press-badge"></span><span class="press-badge"></span>
</div>

<div class="video abs" role="img" aria-label="Video still of the presenter speaking to camera">
  <div class="video-quote abs"><span class="q">"principle of fear"</span>You are helping your bride overcome 3 of the top 15 concerns she has.</div>
</div>
<div class="optin abs">
  <h2>Convince Brides to Choose You Even Before Their Consultation!</h2>
  <div class="field">Your Name</div>
  <div class="field">Your Email</div>
  <div class="btn">Watch Now!</div>
</div>

<svg class="teal-band abs" width="1200" height="420" viewBox="0 0 1200 420">
  <path d="M0 40 C300 -20 600 80 900 40 C1030 20 1120 10 1200 20 L1200 380 C900 420 400 330 0 400Z" fill="var(--teal)"/>
</svg>
<svg class="swoosh abs" width="170" height="14"><path d="M2 10 C50 0 120 0 168 6" stroke="var(--orange)" stroke-width="3" fill="none"/></svg>

<div class="path-card abs" style="left:72px"><svg class="mark" width="110" height="8"><path d="M2 6 C40 0 80 0 108 4" stroke="var(--orange)" stroke-width="2" fill="none"/></svg><h3>I'm New to Selling Wedding Cakes...</h3><div class="more">- Learn More -</div></div>
<div class="path-card abs" style="left:344px"><svg class="mark" width="110" height="8"><path d="M2 6 C40 0 80 0 108 4" stroke="var(--orange)" stroke-width="2" fill="none"/></svg><h3>I want to Maintain My Sales...</h3><div class="more">- Learn More -</div></div>
<div class="path-card abs" style="left:613px"><svg class="mark" width="110" height="8"><path d="M2 6 C40 0 80 0 108 4" stroke="var(--orange)" stroke-width="2" fill="none"/></svg><h3>I'm Eager to Boost My Sales and Profits...</h3><div class="more">- Learn More -</div></div>
<div class="path-card abs" style="left:884px"><svg class="mark" width="110" height="8"><path d="M2 6 C40 0 80 0 108 4" stroke="var(--orange)" stroke-width="2" fill="none"/></svg><h3>I'm Ready to Dominate My Market Area...</h3><div class="more">- Learn More -</div></div>

<article class="feature abs" style="left:72px">
  <div class="feature-img abs" role="img" aria-label="Three chefs holding a trophy sign" style="background:linear-gradient(135deg,#2a2f3a,#5a5560 60%,#a9a9a9)"></div>
  <svg class="feature-wave abs" width="336" height="50"><path d="M0 40 C100 10 230 0 336 10 L336 50 L0 50Z" fill="#fff"/><path d="M0 34 C100 4 230 -6 336 4 L336 14 C230 4 100 14 0 44Z" fill="var(--plum)"/></svg>
  <p>Become the "a Town Favourite." You'll have an atmosphere so special, brides won't think of using anyone but you!</p>
</article>
<article class="feature abs" style="left:434px">
  <div class="feature-img abs" role="img" aria-label="Puzzled woman beside a large question mark" style="background:linear-gradient(135deg,#3a2a2a,#6b5a55 50%,#7b7b7b)"></div>
  <svg class="feature-wave abs" width="336" height="50"><path d="M0 40 C100 10 230 0 336 10 L336 50 L0 50Z" fill="#fff"/><path d="M0 34 C100 4 230 -6 336 4 L336 14 C230 4 100 14 0 44Z" fill="var(--plum)"/></svg>
  <p>Peek at a very effective psychological sales riddle called "The Insecurity Gap."</p>
</article>
<article class="feature abs" style="left:794px">
  <div class="feature-img abs" role="img" aria-label="Split portrait in colour and greyscale" style="background:linear-gradient(90deg,#e9d2b8,#c8ae92 50%,#bdbdbd 50%,#8a8a8a)"></div>
  <svg class="feature-wave abs" width="336" height="50"><path d="M0 40 C100 10 230 0 336 10 L336 50 L0 50Z" fill="#fff"/><path d="M0 34 C100 4 230 -6 336 4 L336 14 C230 4 100 14 0 44Z" fill="var(--plum)"/></svg>
  <p>Discover a sales growth secret that reveals the "Two Faces of Your Wedding Cake Business."</p>
</article>

<h2 class="method-head abs">Use Cutting-edge Methods Proven to Get MORE Leads,<br>Convince MORE Brides to Choose You, Get HIGHER Prices and<br>DOMINATE Your Competition.</h2>

<div class="founder abs">
  <div class="founder-photo" role="img" aria-label="Portrait of the founder in a chef coat"></div>
  <div class="founder-name">Cal Renner</div>
</div>
<div class="method-copy abs">
  <p>Our breakthrough marketing and sales methods are possible due to the long-term studies we've conducted with 150,000 brides over the past 12 years.</p>
  <p>From the findings, we have developed new and revolutionary marketing strategies, sales tools, and a complete transformational wedding cake sales system.</p>
  <p>But, don't take my word for it...let me "prove" the value and impact they will have on your wedding cake business.</p>
</div>
<div class="advisory abs">
  <h3>Enter Your Name and Email Address Below.</h3>
  <p>Each month you'll receive our "Advanced Wedding Cake Marketing Advisory."<br>It's normally available for a $397 subscription fee.</p>
  <strong>You'll receive the first year... absolutely FREE.</strong>
</div>

<svg class="insider-band abs" width="1200" height="500" viewBox="0 0 1200 500">
  <path d="M0 40 C300 -10 700 70 1200 20 L1200 420 C800 360 400 470 0 420Z" fill="var(--teal)"/>
  <path d="M0 420 C400 470 800 360 1200 420 L1200 455 C800 400 400 500 0 460Z" fill="var(--plum)"/>
</svg>
<div class="insider abs">
  <h2>Join our "Insider Advisory" for FREE."</h2>
  <p>You'll receive the latest research secrets while learning how to use psychology for gaining a decisive advantage to market and sell your wedding cakes.</p>
</div>
<div class="insider-form abs">
  <div class="field">Your Name</div>
  <div class="field">Your Email Address</div>
  <div class="btn">Click to Join</div>
</div>

<div class="social abs"><span></span><span></span><span></span></div>
<div class="rule abs"></div>

<footer class="footer-cols abs">
  <div class="footer-col"><h4>MARKETING SOLUTIONS</h4><ul><li>Bridal Insight Starter Course</li><li>Individual Training Videos</li><li>Packaged Training Videos</li><li>Trusted Tier Baker</li><li>Value Lead Marketing Suite</li><li>Analyze Your Marketing</li><li>Premium Ladder Wedding Cake</li></ul></div>
  <div class="footer-col"><h4>MARKETING SOLUTIONS</h4><ul><li>Bridal Insight Starter Course</li><li>Individual Training Videos</li><li>Packaged Training Videos</li><li>Trusted Tier Baker</li><li>Value Lead Marketing Suite</li><li>Analyze Your Marketing</li><li>Premium Ladder Wedding Cake</li></ul></div>
  <div class="footer-col"><h4>MARKETING SOLUTIONS</h4><ul><li>Bridal Insight Starter Course</li><li>Individual Training Videos</li><li>Packaged Training Videos</li><li>Trusted Tier Baker</li><li>Value Lead Marketing Suite</li><li>Analyze Your Marketing</li><li>Premium Ladder Wedding Cake</li></ul></div>
  <div class="footer-col"><h4>MARKETING SOLUTIONS</h4><ul><li>Bridal Insight Starter Course</li><li>Individual Training Videos</li><li>Packaged Training Videos</li><li>Trusted Tier Baker</li><li>Value Lead Marketing Suite</li><li>Analyze Your Marketing</li><li>Premium Ladder Wedding Cake</li></ul></div>
</footer>

</body>
</html>
```